Birchmead Assurance Group Ltd needs a business card and logo

We need a logo for documents, invoices etc and a business card to match. We are a health auditing, training and consulting company based in NZ and working in both Australia and NZ. We ensure health organisations meet all their compliance requirements and develop expertise in the health auditing sector. The design should in some way reflect either symbols for quality management in the health sector.

Target Market(s)

Health providers and those wishing to increase their capability in meeting and understanding compliance requirements

Industry/Entity Type

Business

Contact Information for Business Card

Logo plus contact details

Logo Text

Health auditing, consultancy and training

Requirements
Must have
• Name and contact details director: Clara Hotham, chotham@bag-example.co.nz, PO Box 419, Ridgeford, NZ, cell +6427390516

```html
<!DOCTYPE html>
<html lang="en">
<head>
<meta charset="utf-8">
<title>Clara Hotham — Business Card</title>
<link rel="stylesheet" href="https://fonts.googleapis.com/css2?family=Cinzel:wght@600&family=Montserrat:wght@400&display=swap">
<style>
  :root {
    --paper: #ffffff;
    --rule-grey: #b5b5b5;
    --name-grey: #9e9e9e;
    --contact-blue: #1b8dc0;
    --blue-light: #aee3f6;
    --blue-mid: #0796cb;
    --blue-deep: #0b5a86;
    --globe-tint: #cdeefb;
  }
  html, body {
    margin: 0;
    padding: 0;
    overflow: hidden;
    background: var(--paper);
  }
  .card {
    position: relative;
    width: 1200px;
    height: 683px;
    overflow: hidden;
    background: var(--paper);
  }
  .card-art {
    position: absolute;
    inset: 0;
    width: 1200px;
    height: 683px;
  }
  .top-rule {
    position: absolute;
    left: 0;
    top: 0;
    width: 1120px;
    height: 12px;
    background: var(--rule-grey);
  }
  .name-rule {
    position: absolute;
    left: 8px;
    top: 171px;
    width: 1112px;
    height: 12px;
    background: var(--rule-grey);
  }
  .bottom-rule {
    position: absolute;
    left: 0;
    bottom: 0;
    width: 600px;
    height: 8px;
    background: var(--rule-grey);
  }
  .director-name {
    position: absolute;
    left: 166px;
    top: 58px;
    margin: 0;
    font-family: "Cinzel", "Trajan Pro", serif;
    font-weight: 600;
    font-size: 88px;
    line-height: 1;
    letter-spacing: 2px;
    color: var(--name-grey);
    white-space: nowrap;
  }
  .contact-list {
    position: absolute;
    left: 218px;
    top: 322px;
    margin: 0;
    padding: 0;
    list-style: none;
  }
  .contact-item {
    display: flex;
    align-items: center;
    height: 55px;
    font-family: "Montserrat", "Gotham", sans-serif;
    font-size: 40px;
    color: var(--contact-blue);
    white-space: nowrap;
  }
  .contact-icon {
    width: 36px;
    height: 36px;
    margin-right: 28px;
    flex: none;
  }
</style>
</head>
<body>
  <div class="card">
    <div class="top-rule"></div>

    <svg class="card-art" viewBox="0 0 1200 683" aria-hidden="true">
      <defs>
        <linearGradient id="swoosh-blue" x1="1" y1="0" x2="0.55" y2="1">
          <stop offset="0" stop-color="var(--blue-light)"/>
          <stop offset="0.35" stop-color="var(--blue-mid)"/>
          <stop offset="1" stop-color="var(--blue-deep)"/>
        </linearGradient>
        <radialGradient id="globe-glow" cx="0.5" cy="0.5" r="0.5">
          <stop offset="0" stop-color="var(--globe-tint)" stop-opacity="0.15"/>
          <stop offset="0.85" stop-color="var(--globe-tint)" stop-opacity="0.45"/>
          <stop offset="1" stop-color="var(--globe-tint)" stop-opacity="0"/>
        </radialGradient>
      </defs>
      <path class="swoosh-edge" fill="none" stroke="var(--rule-grey)" stroke-width="38"
        d="M1090 0 L1200 0 L1200 683 L225 683 C300 620 420 585 540 590 C650 595 720 620 840 600 C1000 570 1130 430 1160 260 C1175 160 1140 60 1090 0 Z"/>
      <path class="swoosh-fill" fill="url(#swoosh-blue)"
        d="M1090 0 L1200 0 L1200 683 L225 683 C300 620 420 585 540 590 C650 595 720 620 840 600 C1000 570 1130 430 1160 260 C1175 160 1140 60 1090 0 Z"/>
    </svg>

    <svg class="card-art" viewBox="0 0 1200 683">
      <circle class="globe-motif" role="img" aria-label="Faint globe motif" cx="810" cy="300" r="265" fill="url(#globe-glow)"/>
    </svg>

    <div class="name-rule"></div>
    <div class="bottom-rule"></div>

    <h1 class="director-name">Clara Hotham</h1>

    <ul class="contact-list">
      <li class="contact-item">
        <svg class="contact-icon" viewBox="0 0 36 36" aria-hidden="true">
          <rect x="1.5" y="1.5" width="33" height="33" fill="none" stroke="var(--contact-blue)" stroke-width="2"/>
          <rect x="7" y="10" width="22" height="16" fill="none" stroke="var(--contact-blue)" stroke-width="2"/>
          <path d="M7 10 L18 19 L29 10 M7 26 L15 17 M29 26 L21 17" fill="none" stroke="var(--contact-blue)" stroke-width="1.6"/>
        </svg>
        chotham@bag-example.co.nz
      </li>
      <li class="contact-item">
        <svg class="contact-icon" viewBox="0 0 36 36" aria-hidden="true">
          <rect x="1.5" y="1.5" width="33" height="33" fill="none" stroke="var(--contact-blue)" stroke-width="2"/>
          <path d="M6 19 L18 8 L30 19 L27 19 L27 29 L21 29 L21 22 L15 22 L15 29 L9 29 L9 19 Z" fill="var(--contact-blue)"/>
        </svg>
        PO Box 419, Ridgeford, NZ
      </li>
      <li class="contact-item">
        <svg class="contact-icon" viewBox="0 0 36 36" aria-hidden="true">
          <rect x="1.5" y="1.5" width="33" height="33" fill="none" stroke="var(--contact-blue)" stroke-width="2"/>
          <rect x="12" y="6" width="12" height="24" rx="2" fill="none" stroke="var(--contact-blue)" stroke-width="2"/>
          <rect x="14.5" y="9" width="7" height="8" fill="var(--contact-blue)"/>
          <circle cx="18" cy="25" r="1.8" fill="var(--contact-blue)"/>
        </svg>
        cell +6427390516
      </li>
    </ul>
  </div>
</body>
</html>
```